Company Website for an IT business called "BRIGHT HARBOR"

Complete website creation with text and graphics.
We need :
- modern and creative design for our IT company
- Content management system to edit text later on
- Integrate third party content from partner company
- Contact form (transfer by email)
Updates

Target Market(s)

Small and medium business
private customers

Industry/Entity Type

Information Technology

Coding

Coded - Design and coding required

Number of Pages Required

1 page

Font styles to use
Sans Serif

Requirements
Must have
• Contact form
Link to legal information
Link to data protection (GDPR)
Link to website owner declaration
Nice to have
• Fresh and creative graphics for IT business

```html
<!DOCTYPE html>
<html lang="en">
<head>
<meta charset="utf-8">
<title>BRIGHT HARBOR – IT Consultation &amp; Data Protection</title>
<link href="https://fonts.googleapis.com/css2?family=Ubuntu:wght@300;400;500;700&family=Poppins:wght@400;600&family=Roboto:wght@400&display=swap" rel="stylesheet">
<style>
:root{
  --navy:#0b2a4a;
  --teal:#045b7c;
  --sky:#3aa7dd;
  --button:#0096d6;
  --paper:#f4f4f4;
  --lavender:#efeef8;
  --grey-text:#7a7a7a;
  --white:#ffffff;
}
*{margin:0;padding:0;box-sizing:border-box}
html,body{width:1200px;height:3631px;overflow:hidden}
body{position:relative;background:var(--white);font-family:"Ubuntu",sans-serif;color:var(--navy)}
.abs{position:absolute}

/* hero */
.hero-art{left:0;top:0;width:1200px;height:612px;background:linear-gradient(135deg,#f6f8fa 0%,#e6f1f8 45%,#f4f6f8 100%)}
.hero-rule{left:0;top:609px;width:1200px;height:4px;background:var(--sky);opacity:.6}
.brand{left:66px;top:52px;font-weight:500;font-size:17px;letter-spacing:.5px;color:var(--navy);display:flex;align-items:center;gap:8px}
.brand-mark{width:12px;height:12px;background:var(--sky)}
.nav{right:52px;top:41px;display:flex;gap:15px;font-size:12px;text-transform:uppercase;letter-spacing:.3px}
.nav a{color:var(--navy);text-decoration:none}
.hero-card{left:716px;top:420px;width:474px;height:192px;background:rgba(255,255,255,.92);border:2px solid #bfe0f2;border-bottom:none;padding:28px 28px}
.hero-card h1{font-weight:700;font-size:30px;line-height:41px;letter-spacing:.3px}
.hero-link{display:inline-block;margin:25px 0 0 15px;font-size:15px;color:var(--navy);text-decoration:none;padding-bottom:6px;border-bottom:2px solid var(--button)}

/* intro */
.team-art{left:110px;top:780px;width:422px;height:268px;background:linear-gradient(135deg,#f1f5fb,#dde9f7);border-radius:4px}
.intro{left:666px;top:788px;width:400px}
.section-title{font-weight:700;font-size:32px;line-height:41px;letter-spacing:.3px}
.title-rule{height:3px;background:var(--navy);margin-top:10px}
.intro p{margin-top:28px;font-size:13px;line-height:21px;color:var(--grey-text)}

/* solutions band */
.band{left:0;top:1200px;width:1200px;height:1130px}
.solutions-head{left:0;top:1318px;width:1200px;text-align:center;color:var(--white)}
.solutions-head h2{font-weight:300;font-size:40px}
.solutions-head p{width:680px;margin:22px auto 0;font-size:16px;line-height:21px}
.card{width:456px;height:300px;border:2px solid var(--white);color:var(--white);text-align:center;padding:16px 22px 0}
.card svg{display:block;margin:0 auto;width:90px;height:90px}
.card h3{font-weight:400;font-size:18px;margin-top:12px}
.card-rule{width:252px;height:2px;background:var(--white);margin:28px auto 0}
.card p{font-size:14px;line-height:21px;margin-top:38px}

/* staff */
.paper{left:0;top:2290px;width:1200px;height:1303px;background:var(--paper)}
.staff-art{left:590px;top:2365px;width:360px;height:310px;background:linear-gradient(160deg,#e9eef4,#cfe0f5);border-radius:4px}
.staff{left:165px;top:2497px;width:400px}
.staff .title-rule{width:287px}
.staff p{margin-top:28px;font-size:13px;line-height:21px;color:#555}

/* trend */
.trend{left:113px;top:2763px;width:975px;height:235px;background:var(--teal);color:var(--white);text-align:center;padding:40px 46px 0}
.trend h2{font-weight:700;font-size:31px}
.trend p{margin-top:30px;font-size:13px;line-height:21px}

/* contact */
.contact{left:126px;top:3192px;width:480px}
.contact .title-rule{width:260px}
.contact p{font-size:14px;line-height:21px;color:#444;margin-top:26px}
.contact p + p{margin-top:21px;width:190px}
.form{left:677px;top:3152px;width:388px;font-family:"Poppins",sans-serif}
.field{display:block;width:388px;height:40px;border:1px solid #d6d6d6;border-radius:20px;background:var(--white);font-family:inherit;font-size:13px;color:#888;padding:0 13px;margin-bottom:10px}
.field.message{height:132px;border-radius:20px;padding-top:12px;resize:none}
.send{display:block;width:388px;height:41px;border:none;border-radius:21px;background:var(--button);color:var(--white);font-family:inherit;font-weight:600;font-size:14px;margin-top:1px}

/* footer */
.footer{left:0;top:3593px;width:1200px;height:38px;background:var(--teal);color:var(--white);font-family:"Roboto",sans-serif;font-size:12px;display:flex;justify-content:center;align-items:center;gap:8px}
.footer a{color:var(--white);text-decoration:none}
.footer .sep{width:1px;height:22px;background:var(--white)}
</style>
</head>
<body>

<div class="abs hero-art" role="img" aria-label="Blue wireframe network of connected lines on a light background"></div>
<div class="abs hero-rule"></div>
<div class="abs brand"><span class="brand-mark"></span>BRIGHT HARBOR</div>
<nav class="abs nav"><a href="#">Home</a><a href="#">About</a><a href="#">Solutions</a><a href="#">Staff</a><a href="#">Contact</a></nav>
<div class="abs hero-card">
  <h1>IT Consultation &amp; Data Protection</h1>
  <a class="hero-link" href="#">Welcome</a>
</div>

<div class="abs team-art" role="img" aria-label="Illustration of a small team standing in front of a browser window with app icons"></div>
<section class="abs intro">
  <h2 class="section-title">We Make Customized Solutions For You</h2>
  <div class="title-rule" style="width:197px"></div>
  <p>Lorem ipsum dolor sit amet, consectetur adipiscing elit, sed do eiusmod tempor incididunt ut labore et dolore magna aliqua. Ut enim ad minim veniam, quis nostrud exercitation ullamco laboris nisi ut aliquip ex ea commodo consequat. Duis aute irure dolor in reprehenderit in voluptate velit esse cillum dolore eu fugiat nulla pariatur. Excepteur sint occaecat cupidatat non proident, sunt in culpa qui officia deserunt mollit anim id est laborum</p>
</section>

<div class="abs paper"></div>
<svg class="abs band" viewBox="0 1200 1200 1130" width="1200" height="1130" aria-hidden="true">
  <path d="M0 2225 L0 2310 L1200 2310 L1200 2290 Z" fill="var(--lavender)"/>
  <path d="M0 1262 Q150 1278 400 1252 Q800 1210 1000 1222 Q1100 1226 1200 1228 L1200 2292 Q900 2318 600 2290 Q300 2258 0 2226 Z" fill="var(--teal)"/>
</svg>
<section class="abs solutions-head">
  <h2>Tailor-Made Solutions</h2>
  <p>You just need to know what you want to leave the rest to us. We offer IT solutions to your problem and to your satisfaction. Looking for a web developer? We have your back. Some of our services include:</p>
</section>

<article class="abs card" style="left:126px;top:1514px">
  <svg viewBox="0 0 90 90" fill="none" stroke="#fff" stroke-width="2"><rect x="18" y="4" width="36" height="82" rx="4"/><line x1="18" y1="16" x2="54" y2="16"/><line x1="18" y1="74" x2="54" y2="74"/><rect x="34" y="28" width="46" height="32" rx="2"/><text x="38" y="51" fill="#fff" stroke="none" font-size="18" font-family="Ubuntu">$</text><line x1="52" y1="38" x2="74" y2="38"/><line x1="52" y1="45" x2="74" y2="45"/><line x1="52" y1="52" x2="68" y2="52"/></svg>
  <h3>Accredited Fintech Applications</h3>
  <div class="card-rule"></div>
  <p>Lorem ipsum dolor sit amet, consectetur adipiscing elit, sed do eiusmod tempor incididunt ut labore et dolore magna aliqua.</p>
</article>
<article class="abs card" style="left:618px;top:1514px">
  <svg viewBox="0 0 90 90" fill="none" stroke="#fff" stroke-width="2"><rect x="26" y="26" width="38" height="38" rx="3"/><rect x="36" y="36" width="18" height="18"/><line x1="34" y1="26" x2="34" y2="14"/><line x1="45" y1="26" x2="45" y2="10"/><line x1="56" y1="26" x2="56" y2="14"/><line x1="34" y1="64" x2="34" y2="76"/><line x1="45" y1="64" x2="45" y2="80"/><line x1="56" y1="64" x2="56" y2="76"/><line x1="26" y1="38" x2="14" y2="38"/><line x1="26" y1="52" x2="14" y2="52"/><line x1="64" y1="38" x2="76" y2="38"/><line x1="64" y1="52" x2="76" y2="52"/><circle cx="45" cy="8" r="3"/><circle cx="11" cy="38" r="3"/><circle cx="79" cy="52" r="3"/></svg>
  <h3>Let Artificial Intelligence do it for you.</h3>
  <div class="card-rule"></div>
  <p>Lorem ipsum dolor sit amet, consectetur adipiscing elit, sed do eiusmod tempor incididunt ut labore et dolore magna aliqua.</p>
</article>
<article class="abs card" style="left:126px;top:1850px">
  <svg viewBox="0 0 90 90" fill="none" stroke="#fff" stroke-width="2"><path d="M39 6h12l2 10 8 4 9-5 8 8-5 9 4 8 10 2v12l-10 2-4 8 5 9-8 8-9-5-8 4-2 10H39l-2-10-8-4-9 5-8-8 5-9-4-8-10-2V39l10-2 4-8-5-9 8-8 9 5 8-4z"/><circle cx="45" cy="45" r="14"/><path d="M41 45v26h8V45"/></svg>
  <h3>Create the Service-We Will Handle the Rest</h3>
  <div class="card-rule"></div>
  <p>Lorem ipsum dolor sit amet, consectetur adipiscing elit, sed do eiusmod tempor incididunt ut labore et dolore magna aliqua.</p>
</article>
<article class="abs card" style="left:618px;top:1850px">
  <svg viewBox="0 0 90 90" fill="none" stroke="#fff" stroke-width="2"><circle cx="38" cy="40" r="30"/><circle cx="38" cy="40" r="22"/><polyline points="22,46 32,34 42,44 54,30"/><circle cx="22" cy="46" r="2.5"/><circle cx="54" cy="30" r="2.5"/><path d="M60 62l18 18a4 4 0 0 1-6 6L54 68"/><line x1="66" y1="12" x2="80" y2="6"/><circle cx="82" cy="6" r="3"/></svg>
  <h3>Do the Job-We will do the Analysis.</h3>
  <div class="card-rule"></div>
  <p>Lorem ipsum dolor sit amet, consectetur adipiscing elit, sed do eiusmod tempor incididunt ut labore et dolore magna aliqua.</p>
</article>

<div class="abs staff-art" role="img" aria-label="Illustration of a staff member at a desk on a video call"></div>
<section class="abs staff">
  <h2 class="section-title">Tech-Savvy Staff</h2>
  <div class="title-rule"></div>
  <p>Lorem ipsum dolor sit amet, consectetur adipiscing elit, sed do eiusmod tempor incididunt ut labore et dolore magna aliqua.</p>
</section>

<section class="abs trend">
  <h2>We Set The Trend Or Catch It When It Happens.</h2>
  <p>Lorem ipsum dolor sit amet, consectetur adipiscing elit, sed do eiusmod tempor incididunt ut labore et dolore magna aliqua. Ut enim ad minim veniam, quis nostrud exercitation ullamco laboris nisi ut aliquip ex ea commodo consequat. Duis aute irure dolor in reprehenderit in voluptate velit esse cillum dolore eu fugiat nulla pariatur. Excepteur sint occaecat cupidatat non proident, sunt in culpa qui officia deserunt mollit anim id est laborum</p>
</section>

<section class="abs contact">
  <h2 class="section-title">Get In Touch</h2>
  <div class="title-rule"></div>
  <p>Our team is always eager to hear from you. Whether you want to consult, get a quote or give feedback, we are here to listen and respond.</p>
  <p>Fill the form, and we will get back to you.</p>
</section>
<form class="abs form" action="#" method="post">
  <input class="field" type="text" placeholder="Name">
  <input class="field" type="email" placeholder="Your Email">
  <textarea class="field message" placeholder="Your Message"></textarea>
  <button class="send" type="submit">Send Message</button>
</form>

<footer class="abs footer">
  <a href="#">Copyright © 2020 BRIGHT HARBOR</a><span class="sep"></span><a href="#">BRIGHT HARBOR is fully compliant with the GDPR guidelines.</a>
</footer>

</body>
</html>
```